Perfume Oil manufacturing and distribution company needs an emotion inspiring Wordpress Design

Must be Wordpress Design
Beautiful website needed for a company that manufactures and distributes scents that fragrance products from fine fragrances to personal care and household products. Please refer to attached file (namely "brief" for detailed explanation of our company, product and design requirements)

Website must be beautiful, and not too cluttered.

Must be coded for use in WordPress after design phase

remember not to flood website with pictures of perfumes and perfume bottles, this website is meant to inspire emotion...looking at the big fragrance brands (Valdoret and Morvaleth) one will not see pictures of perfume bottles etc. The site is all about emotion and smell and the senses.
Keep this in mind when submitting designs.

The site must captivate and inspire emotion with beautiful visuals.

the website must be about how one feels when surrounded by a beautiful smell, how one feels confident wearing a good scent. how freshly baked break reminds you of your grandmas house, or how a scent can remind of a seductive encounter, or a memory of fun times with friends out on the town, or as simple as the smell of a good cup of coffee or a rose to inspire a new days happenings.

all this emotion and feeling must be tied into the fact that Aroma Nest makes these moments through great smells. Which we supply to manufacturers of these great end products. whether it is a fine fragrance, a lotion, a car fragrance or a home spray. We scent the world around us.

try not to look too much at our existing website as this is outdated and the company has changed much since then, refer to this and the attached brief

Target Market(s)

small to medium businesses who manufacture products that need to be fragranced. whether these products be prestigious fine fragrances, daily personal care products or home care products, we make the fragrances that make these products beautiful.

Industry/Entity Type

Perfume

Coding

Coded - Design and coding required

Number of Pages Required

5+ page

Font styles to use
Serif
Sans Serif

Colors

Designer to choose colors to be used in the design.

Requirements
Must have
• must have full page header that captivates audience and inspires emotion (through a video or powerful imagery)
• Smell is a powerful emotion trigger and since a computer screen can not produce smell we will need to engage emotion through beautiful imagery and or video and beautiful design on the website. (refer to attached "brief" for more details)
• Must be coded for use in WordPress ONLY after design phase
• site must work well and look great on mobile since most of our audience use mobile to access our site.
Should not have
• too many pictures of perfume packaging and actual products, looking at the big fragrance manufacturers (Valdoret, Morvaleth, KTB) one will not see pictures of perfume bottles and packaging. This is very important as the website is more to inspire emotion and give a sense of how fragrance and perfume makes one feel.
• The site must captivate and inspire emotion with beautiful visuals.

```html
<!DOCTYPE html>
<html lang="en">
<head>
<meta charset="utf-8">
<title>Aroma Nest — Master Perfumers</title>
<link href="https://fonts.googleapis.com/css2?family=Jost:wght@500;600;700&family=Open+Sans:wght@400;600;700&display=swap" rel="stylesheet">
<style>
  :root {
    --dark: #323133;
    --light: #f3f3f3;
    --white: #ffffff;
    --blue: #2f8fd6;
    --blue-deep: #2b86cc;
    --ink: #2f2e30;
    --line: #e1e1e1;
    --hero-top: #6b5650;
    --hero-mid: #4a3834;
    --hero-low: #2e2422;
  }
  * { box-sizing: border-box; margin: 0; padding: 0; }
  html, body { width: 1200px; height: 2228px; overflow: hidden; }
  body { position: relative; background: var(--light); font-family: "Open Sans", sans-serif; color: var(--ink); }

  /* Hero */
  .hero { position: absolute; left: 0; top: 0; width: 1200px; height: 720px;
    background: radial-gradient(ellipse 300px 380px at 600px 380px, #55403a 0%, transparent 70%),
                linear-gradient(180deg, var(--hero-top) 0%, #7a5e55 20%, var(--hero-mid) 50%, var(--hero-low) 100%); }
  .hero-play { position: absolute; left: 552px; top: 360px; width: 96px; height: 96px; }

  .brand { position: absolute; left: 113px; top: 44px; display: flex; align-items: center; gap: 10px; }
  .brand-mark { width: 46px; height: 46px; border-radius: 50%; background: var(--white); }
  .brand-name { font-family: "Jost", sans-serif; font-weight: 700; font-size: 30px; color: var(--white); line-height: 1; }

  .utility-nav { position: absolute; right: 105px; top: 20px; display: flex; gap: 26px; font-size: 12px; color: var(--white); }
  .utility-nav span { display: flex; align-items: center; gap: 5px; }
  .main-nav { position: absolute; right: 110px; top: 60px; display: flex; }
  .main-nav a { font-family: "Jost", sans-serif; font-weight: 600; font-size: 15px; color: var(--white); text-decoration: none;
    padding: 4px 17px; border-left: 1px solid rgba(255,255,255,.75); letter-spacing: .3px; }
  .main-nav a:last-child { border-right: 1px solid rgba(255,255,255,.75); }

  .hero-curve { position: absolute; left: 0; top: 680px; width: 1200px; height: 42px; }

  /* Values */
  .values { position: absolute; left: 0; top: 720px; width: 1200px; height: 560px; background: var(--dark); color: var(--white); }
  .section-title { font-family: "Jost", sans-serif; font-weight: 700; font-size: 38px; text-align: center; letter-spacing: .5px; }
  .values .section-title { position: absolute; top: 70px; width: 100%; }
  .value-list { position: absolute; left: 118px; top: 150px; width: 960px; list-style: none; }
  .value-item { display: flex; gap: 12px; font-size: 16.5px; line-height: 31px; margin-bottom: 24px; }
  .value-item:nth-child(2) { margin-bottom: 34px; }
  .value-item svg { flex: none; width: 34px; height: 34px; margin-top: 0; }
  .value-item strong { font-weight: 700; }
  .btn-about { position: absolute; left: 511px; top: 405px; width: 178px; height: 54px; border-radius: 27px; background: var(--blue);
    color: var(--white); font-family: "Jost", sans-serif; font-weight: 700; font-size: 21px; display: flex; align-items: center; justify-content: center; gap: 10px; }

  /* Products */
  .products { position: absolute; left: 0; top: 1280px; width: 1200px; height: 600px; }
  .products .section-title { position: absolute; top: 56px; width: 100%; color: var(--ink); }
  .product-card { position: absolute; top: 168px; width: 225px; height: 322px; background: var(--white); border: 1px solid var(--line);
    box-shadow: 0 1px 3px rgba(0,0,0,.06); text-align: center; }
  .product-shot { position: absolute; left: 50%; bottom: 130px; transform: translateX(-50%); border-radius: 8px 8px 6px 6px;
    background: linear-gradient(90deg, #d9d9d6 0%, #ffffff 40%, #e6e6e3 100%); box-shadow: 2px 3px 6px rgba(0,0,0,.15); }
  .product-name { position: absolute; top: 210px; width: 100%; font-weight: 700; font-size: 18px; color: var(--blue); }
  .btn-more { position: absolute; left: 47px; top: 259px; width: 131px; height: 38px; border: 2px solid var(--blue); border-radius: 19px;
    font-weight: 600; font-size: 14px; color: var(--blue); display: flex; align-items: center; justify-content: center; }

  /* Footer */
  .footer { position: absolute; left: 0; top: 1864px; width: 1200px; height: 364px;
    background: radial-gradient(ellipse 240px 160px at 530px 130px, rgba(120,180,230,.45), transparent 70%),
                radial-gradient(ellipse 260px 180px at 920px 110px, rgba(30,90,150,.35), transparent 70%),
                linear-gradient(180deg, #3a95d8 0%, var(--blue-deep) 100%); color: var(--white); }
  .footer-curve { position: absolute; left: 0; top: 0; width: 1200px; height: 34px; }
  .contact-title { position: absolute; left: 113px; top: 112px; font-family: "Jost", sans-serif; font-weight: 700; font-size: 25px; }
  .contact-email { position: absolute; left: 113px; top: 163px; display: flex; align-items: center; gap: 14px; font-size: 26px; }
  .btn-callback { position: absolute; left: 572px; top: 141px; width: 279px; height: 62px; border-radius: 31px; background: var(--white);
    color: var(--blue); font-weight: 700; font-size: 22px; display: flex; align-items: center; justify-content: center; gap: 14px; }
  .social-tab { position: absolute; left: 1028px; top: 84px; width: 61px; height: 168px; background: #2d4a8a; }
  .social-tab span { position: absolute; left: 16px; top: 18px; writing-mode: vertical-rl; font-weight: 700; font-size: 25px; color: var(--white); }
  .social-dot { position: absolute; left: 1012px; top: 153px; width: 32px; height: 32px; border-radius: 50%; background: #3a7de0; border: 2px solid var(--white); }
  .footer-rule { position: absolute; left: 113px; top: 292px; width: 974px; height: 1px; background: rgba(255,255,255,.25); }
  .copyright { position: absolute; top: 316px; width: 100%; text-align: center; font-size: 13px; }
  .build-code { position: absolute; right: 16px; top: 316px; font-size: 13px; }
</style>
</head>
<body>

<header class="hero" role="img" aria-label="Woman in a hat seen from behind, looking over a hazy valley at sunset">
  <div class="brand"><span class="brand-mark"></span><span class="brand-name">Aroma Nest</span></div>

  <nav class="utility-nav">
    <span>✎ ONLINE TRAINING</span>
    <span>■ CAREERS</span>
    <span>☏ CONTACT US</span>
    <span>
      <svg width="12" height="12" viewBox="0 0 12 12"><circle cx="5" cy="5" r="3.5" fill="none" stroke="#fff" stroke-width="1.6"/><line x1="7.5" y1="7.5" x2="11" y2="11" stroke="#fff" stroke-width="1.8"/></svg>
    </span>
  </nav>

  <nav class="main-nav">
    <a href="#">HOME</a><a href="#">AROMA NEST</a><a href="#">OUR SERVICES</a><a href="#">OUR PRODUCTS</a><a href="#">BLOG</a>
  </nav>

  <svg class="hero-play" viewBox="0 0 96 96">
    <circle cx="48" cy="48" r="45" fill="none" stroke="#fff" stroke-width="4" opacity=".9"/>
    <path d="M38 30 L66 48 L38 66 Z" fill="none" stroke="#fff" stroke-width="4" stroke-linejoin="round" opacity=".9"/>
  </svg>
</header>

<svg class="hero-curve" viewBox="0 0 1200 42" preserveAspectRatio="none">
  <path d="M0 6 Q600 58 1200 6 L1200 42 L0 42 Z" fill="#323133"/>
</svg>

<section class="values">
  <h2 class="section-title">AROMA NEST</h2>
  <ul class="value-list">
    <li class="value-item">
      <svg viewBox="0 0 34 34" fill="none" stroke="#fff" stroke-width="1.4"><path d="M6 28 L22 12 L26 16 L10 32 Z"/><path d="M22 12 L28 6 L32 10 L26 16"/><path d="M4 22 L12 14"/></svg>
      <p><strong>Legitimacy</strong> (over 80 years combined experience, industry affiliations with packaging, ethanol and chemicals give us the edge in truly understanding the industry in which we operate)</p>
    </li>
    <li class="value-item">
      <svg viewBox="0 0 34 34" fill="none" stroke="#fff" stroke-width="1.4"><path d="M17 3 L22 8 L19 8 L19 15 L26 15 L26 12 L31 17 L26 22 L26 19 L19 19 L19 26 L22 26 L17 31 L12 26 L15 26 L15 19 L8 19 L8 22 L3 17 L8 12 L8 15 L15 15 L15 8 L12 8 Z"/></svg>
      <p><strong>Servanthood</strong> (we are here to serve each stakeholder: customers, suppliers, employees and shareholders)</p>
    </li>
    <li class="value-item">
      <svg viewBox="0 0 34 34" fill="none" stroke="#fff" stroke-width="1.4"><path d="M11 17 A6 6 0 1 1 23 17 C23 20 20 21 20 25 L14 25 C14 21 11 20 11 17 Z"/><path d="M14 28 L20 28 M15 31 L19 31"/><path d="M17 4 V7 M6 10 L8 12 M28 10 L26 12 M3 19 H6 M28 19 H31"/></svg>
      <p><strong>Execution</strong> (99% done = ZERO% done, if it is not done until it is 100% done, we are pedantic about result orientated service)</p>
    </li>
  </ul>
  <div class="btn-about">ABOUT
    <svg width="18" height="18" viewBox="0 0 18 18"><circle cx="9" cy="9" r="9" fill="#fff"/><path d="M5 9 H12 M9 5.5 L12.5 9 L9 12.5" stroke="#2f8fd6" stroke-width="2.2" fill="none"/></svg>
  </div>
</section>

<section class="products">
  <h2 class="section-title">OUR PRODUCTS</h2>
  <article class="product-card" style="left:113px">
    <div class="product-shot" role="img" aria-label="Small 100g perfume oil jar" style="width:38px;height:72px"></div>
    <h3 class="product-name">100G PERFUME OIL</h3>
    <div class="btn-more">VIEW MORE</div>
  </article>
  <article class="product-card" style="left:362px">
    <div class="product-shot" role="img" aria-label="200g perfume oil jar" style="width:50px;height:104px"></div>
    <h3 class="product-name">200G PERFUME OIL</h3>
    <div class="btn-more">VIEW MORE</div>
  </article>
  <article class="product-card" style="left:612px">
    <div class="product-shot" role="img" aria-label="500g perfume oil bottle" style="width:56px;height:138px"></div>
    <h3 class="product-name">500G PERFUME OIL</h3>
    <div class="btn-more">VIEW MORE</div>
  </article>
  <article class="product-card" style="left:862px">
    <div class="product-shot" role="img" aria-label="1kg perfume oil bottle" style="width:46px;height:146px"></div>
    <h3 class="product-name">1KG PERFUME OIL</h3>
    <div class="btn-more">VIEW MORE</div>
  </article>
</section>

<footer class="footer" role="img" aria-label="Blue-toned roses and a tipped perfume bottle behind the contact details">
  <svg class="footer-curve" viewBox="0 0 1200 34" preserveAspectRatio="none">
    <path d="M0 0 L0 30 Q600 -26 1200 30 L1200 0 Z" fill="#f3f3f3"/>
  </svg>
  <h3 class="contact-title">CONTACT ME</h3>
  <p class="contact-email">
    <svg width="26" height="20" viewBox="0 0 26 20"><rect width="26" height="20" rx="2" fill="#fff"/><path d="M1 2 L13 11 L25 2" stroke="#2f8fd6" stroke-width="2" fill="none"/></svg>
    nadia@aromanest.co.za
  </p>
  <div class="btn-callback">
    <svg width="28" height="28" viewBox="0 0 28 28" fill="none" stroke="#2f8fd6" stroke-width="1.8"><path d="M7 3 L11 8 L8.5 11 C10 15 13 18 17 19.5 L20 17 L25 21 L22 25 C13 25 3 15 3 6 Z"/><path d="M16 3 A9 9 0 0 1 25 12 M16 7 A5 5 0 0 1 21 12"/></svg>
    CALL ME BACK
  </div>
  <div class="social-tab"><span>Chatterly</span></div>
  <div class="social-dot"></div>
  <div class="footer-rule"></div>
  <p class="copyright">© 2018 Aroma Nest.&nbsp; All rights reserved.&nbsp; Term of Use</p>
  <p class="build-code">C16</p>
</footer>

</body>
</html>
```